Powerpoint Presentation Template

Kindly design a business class Powepoint Presentation template for our business use. Please stick to our company colours or even pictures as shown on our website and Logo

```html
<!DOCTYPE html>
<html lang="en">
<head>
<meta charset="utf-8">
<title>Kestrel Properties – Presentation Template</title>
<link rel="stylesheet" href="https://fonts.googleapis.com/css2?family=Open+Sans:wght@400;600;700;800&display=swap">
<style>
:root{
  --maroon:#7c2d22;
  --maroon-dark:#5e2119;
  --maroon-soft:#a8574b;
  --blush:#d9b3ac;
  --ink:#262626;
  --charcoal:#2b2b2b;
  --grey:#8a8a8a;
  --grey-light:#d6d6d6;
  --text:#444;
  --paper:#ffffff;
  --canvas:#e9e9e9;
}
*{box-sizing:border-box;margin:0;padding:0}
html,body{width:1200px;height:2278px;overflow:hidden;background:var(--canvas)}
body{font-family:'Open Sans',Arial,sans-serif}
.deck{display:grid;grid-template-columns:repeat(3,358px);grid-auto-rows:269px;column-gap:24px;row-gap:11px;padding:26px 43px}
.slide{position:relative;overflow:hidden;background:var(--paper);box-shadow:0 1px 3px rgba(0,0,0,.18)}
.abs{position:absolute}
.fill{position:absolute;inset:0;width:100%;height:100%}
.photo{position:absolute}
.hdr{position:absolute;left:22px;top:15px;font:700 12.5px/1 'Open Sans',sans-serif;color:var(--ink);letter-spacing:.2px}
.hdr::before{content:"";position:absolute;left:-22px;top:-1px;width:14px;height:14px;background:var(--maroon);clip-path:polygon(0 0,100% 0,55% 100%,0 100%)}
.hdr.light{color:#fff}
.brand{position:absolute;right:9px;top:9px;font:700 7px/1.05 'Open Sans',sans-serif;color:var(--maroon);text-align:right}
.brand.light{color:#fff}
.foot{position:absolute;left:0;right:0;bottom:0;height:11px;background:var(--maroon)}
.foot .copy{position:absolute;left:10px;top:2.5px;font:400 4.5px/1 'Open Sans',sans-serif;color:#fff}
.foot .num{position:absolute;right:0;top:0;height:11px;width:40px;background:var(--ink);clip-path:polygon(22% 0,100% 0,100% 100%,0 100%);font:600 6px/11px 'Open Sans',sans-serif;color:#fff;text-align:right;padding-right:8px}
.p{font:400 6px/1.5 'Open Sans',sans-serif;color:var(--text)}
.p.b{font-weight:700;color:var(--ink)}
.p.w{color:#fff}
.h6{font:700 6px/1.3 'Open Sans',sans-serif;color:var(--ink)}
.h6.m{color:var(--maroon)}
.h6.w{color:#fff}
.bul{list-style:none}
.bul li{position:relative;padding-left:9px;font:400 5.5px/1.9 'Open Sans',sans-serif;color:var(--text)}
.bul li::before{content:"";position:absolute;left:1px;top:4px;width:4px;height:3px;background:var(--maroon);clip-path:polygon(0 0,100% 50%,0 100%)}
.url{position:absolute;left:24px;bottom:9px;font:400 5px/1 'Open Sans',sans-serif;color:var(--text)}
.title-lg{font:700 16px/1.1 'Open Sans',sans-serif;color:var(--maroon)}
.sub{font:400 8.5px/1.3 'Open Sans',sans-serif;color:var(--ink)}
.brand-lg{font:700 19px/1 'Open Sans',sans-serif;color:var(--maroon)}
</style>
</head>
<body>
<main class="deck">

<!-- 1 cover -->
<section class="slide">
  <svg class="fill" viewBox="0 0 358 269" aria-hidden="true">
    <defs><linearGradient id="g1" x1="0" y1="0" x2="1" y2="1"><stop offset="0" stop-color="#9a8f96"/><stop offset="1" stop-color="#6b4a45"/></linearGradient></defs>
  </svg>
  <div class="photo" role="img" aria-label="Modern residential building photograph" style="left:0;top:0;width:358px;height:269px;clip-path:polygon(145px 0,358px 0,358px 269px,262px 269px);background:linear-gradient(135deg,#a39ca3,#6e5753)"></div>
  <svg class="fill" viewBox="0 0 358 269" aria-hidden="true">
    <polygon points="205,128 358,8 358,269 190,269" fill="#7c2d22" opacity=".85"/>
    <line x1="145" y1="0" x2="262" y2="269" stroke="#fff" stroke-width="1.5"/>
  </svg>
  <div class="abs brand-lg" style="left:24px;top:48px">Kestrel<br>Properties</div>
  <div class="abs title-lg" style="left:24px;top:140px">PRESENTATION TITLE</div>
  <div class="abs sub" style="left:24px;top:160px">Presentation Subtitle Goes Here</div>
  <div class="url">WWW.KESTRELPROP.CO.ZA</div>
</section>

<!-- 2 cover alt -->
<section class="slide">
  <svg class="fill" viewBox="0 0 358 269" aria-hidden="true">
    <polygon points="140,0 358,0 358,15 250,135" fill="#7c2d22"/>
    <polygon points="250,135 358,15 358,255" fill="#262626"/>
    <polygon points="250,135 358,255 358,269 118,269" fill="#7c2d22"/>
  </svg>
  <div class="abs brand-lg" style="left:24px;top:48px">Kestrel<br>Properties</div>
  <div class="abs title-lg" style="left:24px;top:140px">PRESENTATION TITLE</div>
  <div class="abs sub" style="left:24px;top:160px">Presentation Subtitle Goes Here</div>
  <div class="url">WWW.KESTRELPROP.CO.ZA</div>
</section>

<!-- 3 cover image -->
<section class="slide">
  <div class="photo" role="img" aria-label="Greyscale photograph of an apartment building" style="inset:0;background:linear-gradient(120deg,#eeeeee,#c9c9c9 60%,#b5b5b5)"></div>
  <svg class="fill" viewBox="0 0 358 269" aria-hidden="true">
    <polygon points="200,135 358,0 358,269" fill="#262626"/>
    <polygon points="200,135 358,0 290,0" fill="#7c2d22"/>
    <line x1="200" y1="0" x2="358" y2="269" stroke="#fff" stroke-width="1.2"/>
  </svg>
  <div class="abs brand-lg" style="left:62px;top:100px;font-size:26px">Kestrel</div>
  <div class="url">WWW.KESTRELPROP.CO.ZA</div>
</section>

<!-- 4 agenda list -->
<section class="slide">
  <div class="photo" role="img" aria-label="Maroon-toned property photograph" style="left:0;top:0;width:358px;height:269px;clip-path:polygon(0 0,200px 0,140px 269px,0 269px);background:linear-gradient(160deg,#8f3a2e,#6d271e)"></div>
  <div class="abs" style="left:28px;top:36px;font:700 13px/1 'Open Sans',sans-serif;color:#fff">OUR AGENDA</div>
  <div class="brand" style="top:16px;right:18px;font-size:8px">Kestrel</div>
  <ul class="bul abs" style="left:212px;top:70px">
    <li style="font:600 8.5px/2.1 'Open Sans',sans-serif;color:var(--ink);padding-left:12px">About Us</li>
    <li style="font:600 8.5px/2.1 'Open Sans',sans-serif;color:var(--ink);padding-left:12px">Our Mission</li>
    <li style="font:600 8.5px/2.1 'Open Sans',sans-serif;color:var(--ink);padding-left:12px">How It Works</li>
    <li style="font:600 8.5px/2.1 'Open Sans',sans-serif;color:var(--ink);padding-left:12px">Our Vision</li>
    <li style="font:600 8.5px/2.1 'Open Sans',sans-serif;color:var(--ink);padding-left:12px">Graphic Chart</li>
    <li style="font:600 8.5px/2.1 'Open Sans',sans-serif;color:var(--ink);padding-left:12px">The Services</li>
    <li style="font:600 8.5px/2.1 'Open Sans',sans-serif;color:var(--ink);padding-left:12px">Contact Page</li>
  </ul>
</section>

<!-- 5 agenda timetable -->
<section class="slide">
  <div class="photo" role="img" aria-label="Maroon-tinted photograph of houses" style="inset:0;background:linear-gradient(150deg,#8a3a2f,#6e2a21)"></div>
  <svg class="fill" viewBox="0 0 358 269" aria-hidden="true">
    <polygon points="12,0 122,0 122,150 12,180" fill="#262626"/>
    <polygon points="12,180 122,150 122,158 12,190" fill="#fff"/>
  </svg>
  <div class="abs" style="left:24px;top:60px;font:700 9px/1 'Open Sans',sans-serif;color:var(--maroon-soft)">OUR AGENDA</div>
  <p class="abs p w" style="left:24px;top:74px;width:88px;font-size:5.5px">Lorem ipsum dolor sit amet, consectetur adipisicing elit, sed do eiusmod tempor incididunt ut labore et dolore magna aliqua.</p>
  <div class="abs" style="left:140px;top:48px;display:grid;grid-template-columns:105px 105px;row-gap:16px">
    <div><div class="h6 w">9:05 AM<br>HEADING TEXT</div><p class="p w" style="font-size:5px;margin-top:3px">Lorem ipsum dolor sit amet, consectetur adipisicing elit, sed do eiusmod tempor incididunt.</p></div>
    <div><div class="h6 w">9:05 AM<br>HEADING TEXT</div><p class="p w" style="font-size:5px;margin-top:3px">Lorem ipsum dolor sit amet, consectetur adipisicing elit, sed do eiusmod tempor incididunt.</p></div>
    <div><div class="h6 w">9:05 AM<br>HEADING TEXT</div><p class="p w" style="font-size:5px;margin-top:3px">Lorem ipsum dolor sit amet, consectetur adipisicing elit, sed do eiusmod tempor incididunt.</p></div>
    <div><div class="h6 w">9:05 AM<br>HEADING TEXT</div><p class="p w" style="font-size:5px;margin-top:3px">Lorem ipsum dolor sit amet, consectetur adipisicing elit, sed do eiusmod tempor incididunt.</p></div>
    <div><div class="h6 w">9:05 AM<br>HEADING TEXT</div><p class="p w" style="font-size:5px;margin-top:3px">Lorem ipsum dolor sit amet, consectetur adipisicing elit, sed do eiusmod tempor incididunt.</p></div>
  </div>
</section>

<!-- 6 welcome -->
<section class="slide">
  <div class="abs" style="left:0;top:14px;width:10px;height:14px;background:var(--maroon);clip-path:polygon(0 0,100% 0,55% 100%,0 100%)"></div>
  <div class="abs" style="left:22px;top:14px;font:700 13px/1 'Open Sans',sans-serif;color:var(--ink)">WELCOME</div>
  <div class="abs" style="left:22px;top:30px;font:600 6px/1 'Open Sans',sans-serif;color:var(--maroon)">MESSAGE</div>
  <p class="abs p" style="left:22px;top:98px;width:160px">Lorem ipsum dolor sit amet, consectetur adipisicing elit, sed do eiusmod tempor incididunt ut labore et dolore magna aliqua. Ut enim ad minim veniam, quis nostrud exercitation ullamco laboris nisi ut aliquip ex ea commodo consequat.</p>
  <p class="abs p" style="left:22px;top:160px;width:160px">Duis aute irure dolor in reprehenderit in voluptate velit esse cillum dolore eu fugiat nulla pariatur.</p>
  <div class="photo" role="img" aria-label="Photograph of a smiling businesswoman shaking hands" style="left:198px;top:10px;width:160px;height:237px;background:linear-gradient(160deg,#d8d2cc,#9f8a7b 60%,#5c4a40)"></div>
  <div class="brand">Kestrel<br>Properties</div>
  <div class="foot"><span class="copy">© Copyright text here</span><span class="num">1</span></div>
</section>

<!-- 7 header + bullets -->
<section class="slide">
  <div class="hdr">HEADER TEXT GOES HERE</div>
  <div class="brand">Kestrel<br>Properties</div>
  <p class="abs p b" style="left:22px;top:76px;width:316px;font-size:5.8px">Lorem ipsum dolor sit amet, consectetur adipisicing elit, sed do eiusmod tempor incididunt ut labore et dolore magna aliqua. Ut enim ad minim veniam, quis</p>
  <p class="abs p" style="left:22px;top:92px;width:316px;font-size:5.8px">nostrud exercitation ullamco laboris nisi ut aliquip ex ea commodo consequat. Duis aute irure dolor in reprehenderit in voluptate velit esse cillum dolore eu fugiat nulla pariatur.</p>
  <ul class="bul abs" style="left:52px;top:132px">
    <li>Lorem ipsum dolor sit amet</li><li>Ut enim ad minim veniam</li><li>Incididunt ut labore et dolore magna</li><li>Esse cillum dolore eu fugiat nulla pariatur</li><li>Dolore in reprehenderit in voluptate</li><li>Nisi ut aliquip ex ea</li>
  </ul>
  <div class="foot"><span class="copy">© Copyright text here</span><span class="num">2</span></div>
</section>

<!-- 8 steps -->
<section class="slide">
  <div class="photo" role="img" aria-label="Photograph of a suburban house with driveway" style="left:0;top:0;width:358px;height:118px;background:linear-gradient(170deg,#b89c8c,#7d5c4d 60%,#8a7466)"></div>
  <div class="brand light">Kestrel<br>Properties</div>
  <svg class="abs" style="left:0;top:0" width="358" height="269" aria-hidden="true">
    <line x1="20" y1="124" x2="338" y2="124" stroke="#cfcfcf" stroke-width="1"/>
    <circle cx="63" cy="124" r="14" fill="#262626" stroke="#fff" stroke-width="2"/>
    <circle cx="179" cy="124" r="14" fill="#7c2d22" stroke="#fff" stroke-width="2"/>
    <circle cx="294" cy="124" r="14" fill="#8a8a8a" stroke="#fff" stroke-width="2"/>
    <text x="63" y="128" font-family="Open Sans, sans-serif" font-weight="700" font-size="10" fill="#fff" text-anchor="middle">1</text>
    <text x="179" y="128" font-family="Open Sans, sans-serif" font-weight="700" font-size="10" fill="#fff" text-anchor="middle">2</text>
    <text x="294" y="128" font-family="Open Sans, sans-serif" font-weight="700" font-size="10" fill="#fff" text-anchor="middle">3</text>
  </svg>
  <div class="abs" style="left:20px;top:155px;width:90px"><div class="h6" style="font-size:5px">TEXT GOES HERE</div><p class="p" style="font-size:4.8px">Lorem ipsum dolor sit amet, consectetur adipisicing elit, sed do eiusmod tempor.</p></div>
  <div class="abs" style="left:136px;top:155px;width:90px"><div class="h6" style="font-size:5px">TEXT GOES HERE</div><p class="p" style="font-size:4.8px">Lorem ipsum dolor sit amet, consectetur adipisicing elit, sed do eiusmod tempor.</p></div>
  <div class="abs" style="left:251px;top:155px;width:90px"><div class="h6" style="font-size:5px">TEXT GOES HERE</div><p class="p" style="font-size:4.8px">Lorem ipsum dolor sit amet, consectetur adipisicing elit, sed do eiusmod tempor.</p></div>
  <div class="foot"><span class="copy">© Copyright text here</span><span class="num">3</span></div>
</section>

<!-- 9 header + highlight box -->
<section class="slide">
  <div class="hdr">HEADER TEXT GOES HERE</div>
  <div class="brand">Kestrel<br>Properties</div>
  <div class="abs" style="left:22px;top:84px;width:314px;height:42px;background:var(--maroon);padding:6px 8px">
    <p class="p w" style="font-weight:700;font-size:5.8px">Lorem ipsum dolor sit amet, consectetur adipisicing elit, sed do eiusmod tempor incididunt ut labore et dolore magna aliqua. Ut enim ad minim veniam, quis nostrud exercitation ullamco laboris nisi ut aliquip ex ea commodo consequat.</p>
  </div>
  <p class="abs p" style="left:22px;top:144px;width:314px">Lorem ipsum dolor sit amet, consectetur adipisicing elit, sed do eiusmod tempor incididunt ut labore et dolore magna aliqua. Ut enim ad minim veniam, quis nostrud exercitation ullamco laboris nisi ut aliquip ex ea commodo consequat. Duis aute irure dolor in reprehenderit in voluptate velit esse cillum dolore eu fugiat nulla pariatur. Excepteur sint occaecat cupidatat non proident, sunt in culpa qui officia deserunt mollit anim id est laborum.</p>
  <div class="foot"><span class="copy">© Copyright text here</span><span class="num">4</span></div>
</section>

<!-- 10 subheading paragraphs -->
<section class="slide">
  <div class="hdr">HEADER TEXT GOES HERE</div>
  <div class="brand">Kestrel<br>Properties</div>
  <div class="abs h6" style="left:22px;top:70px;font-size:6.5px">SUBHEADING GOES HERE</div>
  <p class="abs p" style="left:22px;top:84px;width:314px;font-size:6.3px">Lorem ipsum dolor sit amet, consectetur adipisicing elit, sed do eiusmod tempor incididunt ut labore et dolore magna aliqua. Ut enim ad minim veniam, quis nostrud exercitation ullamco laboris nisi ut aliquip ex ea commodo consequat. Duis aute irure dolor in reprehenderit in voluptate velit esse cillum dolore eu fugiat nulla pariatur.</p>
  <p class="abs p" style="left:22px;top:150px;width:314px;font-size:6.3px">Lorem ipsum dolor sit amet, consectetur adipisicing elit, sed do eiusmod tempor incididunt ut labore et dolore magna aliqua. Ut enim ad minim veniam, quis nostrud exercitation ullamco laboris nisi ut aliquip ex ea commodo consequat. Duis aute irure dolor in reprehenderit in voluptate velit esse cillum dolore eu fugiat nulla pariatur.</p>
  <div class="foot"><span class="copy">© Copyright text here</span><span class="num">5</span></div>
</section>

<!-- 11 image with three feature boxes -->
<section class="slide">
  <div class="photo" role="img" aria-label="Photograph of steel scaffolding and stairs with a soft maroon overlay" style="inset:0;background:linear-gradient(120deg,#6d5551,#c7a39c 45%,#d9b3ac)"></div>
  <div class="brand">Kestrel<br>Properties</div>
  <div class="abs" style="left:25px;top:100px;width:92px;height:98px;background:var(--charcoal);text-align:center;padding-top:14px">
    <svg width="16" height="14" viewBox="0 0 16 14" aria-hidden="true"><polyline points="1,12 5,7 8,9 14,2" fill="none" stroke="#fff" stroke-width="1.5"/><line x1="1" y1="13" x2="15" y2="13" stroke="#fff"/></svg>
    <div class="h6 w" style="margin-top:4px">HEADING TEXT</div><p class="p w" style="font-size:4.8px;padding:2px 8px">Lorem ipsum dolor sit amet, consectetur adipisicing elit, sed do eiusmod tempor.</p>
  </div>
  <div class="abs" style="left:134px;top:100px;width:92px;height:98px;background:var(--maroon);text-align:center;padding-top:14px">
    <svg width="18" height="14" viewBox="0 0 18 14" aria-hidden="true"><circle cx="9" cy="4" r="3" fill="#fff"/><path d="M3 14a6 5 0 0 1 12 0z" fill="#fff"/><circle cx="3" cy="5" r="2" fill="#fff"/><circle cx="15" cy="5" r="2" fill="#fff"/></svg>
    <div class="h6 w" style="margin-top:4px">HEADING TEXT</div><p class="p w" style="font-size:4.8px;padding:2px 8px">Lorem ipsum dolor sit amet, consectetur adipisicing elit, sed do eiusmod tempor.</p>
  </div>
  <div class="abs" style="left:243px;top:100px;width:92px;height:98px;background:var(--charcoal);text-align:center;padding-top:14px">
    <svg width="14" height="14" viewBox="0 0 14 14" aria-hidden="true"><circle cx="7" cy="7" r="6" fill="#fff"/><text x="7" y="10" font-size="8" font-weight="700" text-anchor="middle" fill="#2b2b2b" font-family="Open Sans, sans-serif">$</text></svg>
    <div class="h6 w" style="margin-top:4px">HEADING TEXT</div><p class="p w" style="font-size:4.8px;padding:2px 8px">Lorem ipsum dolor sit amet, consectetur adipisicing elit, sed do eiusmod tempor.</p>
  </div>
</section>

<!-- 12 icon grid -->
<section class="slide">
  <div class="hdr">HEADER TEXT GOES HERE</div>
  <div class="brand">Kestrel<br>Properties</div>
  <div class="abs" style="left:40px;top:98px;width:90px"><svg width="12" height="12" viewBox="0 0 12 12" aria-hidden="true"><rect x="1" y="3" width="4" height="9" fill="none" stroke="#7c2d22"/><rect x="6" y="0" width="5" height="12" fill="none" stroke="#7c2d22"/></svg><div class="h6 m" style="font-size:5.5px">HEADING TEXT</div><p class="p" style="font-size:4.6px">Lorem ipsum dolor sit amet, consectetur adipisicing elit, sed do eiusmod tempor.</p></div>
  <div class="abs" style="left:140px;top:98px;width:90px"><svg width="12" height="12" viewBox="0 0 12 12" aria-hidden="true"><path d="M6 11C3 7 2 5.5 2 4a4 4 0 0 1 8 0c0 1.5-1 3-4 7z" fill="none" stroke="#7c2d22"/><circle cx="6" cy="4" r="1.3" fill="#7c2d22"/></svg><div class="h6 m" style="font-size:5.5px">HEADING TEXT</div><p class="p" style="font-size:4.6px">Lorem ipsum dolor sit amet, consectetur adipisicing elit, sed do eiusmod tempor.</p></div>
  <div class="abs" style="left:242px;top:98px;width:90px"><svg width="12" height="12" viewBox="0 0 12 12" aria-hidden="true"><path d="M1 6L6 1l5 5M3 5v6h6V5" fill="none" stroke="#7c2d22"/></svg><div class="h6 m" style="font-size:5.5px">HEADING TEXT</div><p class="p" style="font-size:4.6px">Lorem ipsum dolor sit amet, consectetur adipisicing elit, sed do eiusmod tempor.</p></div>
  <div class="abs" style="left:40px;top:168px;width:90px"><svg width="12" height="12" viewBox="0 0 12 12" aria-hidden="true"><path d="M1 2h10v6H5l-3 3V8H1z" fill="none" stroke="#7c2d22"/></svg><div class="h6 m" style="font-size:5.5px">HEADING TEXT</div><p class="p" style="font-size:4.6px">Lorem ipsum dolor sit amet, consectetur adipisicing elit, sed do eiusmod tempor.</p></div>
  <div class="abs" style="left:140px;top:168px;width:90px"><svg width="12" height="12" viewBox="0 0 12 12" aria-hidden="true"><circle cx="4" cy="4" r="2" fill="none" stroke="#7c2d22"/><circle cx="9" cy="5" r="1.6" fill="none" stroke="#7c2d22"/><path d="M0 11a4 3.5 0 0 1 8 0M7 11a3 3 0 0 1 5 0" fill="none" stroke="#7c2d22"/></svg><div class="h6 m" style="font-size:5.5px">HEADING TEXT</div><p class="p" style="font-size:4.6px">Lorem ipsum dolor sit amet, consectetur adipisicing elit, sed do eiusmod tempor.</p></div>
  <div class="foot"><span class="copy">© Copyright text here</span><span class="num">6</span></div>
</section>

<!-- 13 section break -->
<section class="slide" style="background:var(--maroon)">
  <svg class="fill" viewBox="0 0 358 269" aria-hidden="true">
    <polygon points="0,0 90,0 200,269 60,269" fill="#8a3529" opacity=".6"/>
    <polygon points="260,0 358,0 358,269 320,269" fill="#6a251c" opacity=".6"/>
  </svg>
  <div class="abs" style="left:30px;right:30px;top:102px;text-align:center;color:#fff">
    <div style="font:700 9px/1.3 'Open Sans',sans-serif">SECTION BREAK OR OTHER TITLE HERE</div>
    <p style="font:400 8.2px/1.35 'Open Sans',sans-serif;margin-top:3px">Lorem ipsum dolor sit amet, consectetur adipisicing elit, sed do eiusmod tempor incididunt ut labore et dolore magna aliqua. Ut enim ad minim veniam, quis nostrud exercitation ullamco laboris nisi ut aliquip ex ea commodo consequat.</p>
  </div>
</section>

<!-- 14 horizontal bar chart -->
<section class="slide">
  <div class="hdr">HEADER TEXT GOES HERE</div>
  <div class="brand">Kestrel<br>Properties</div>
  <svg class="abs" style="left:20px;top:60px" width="320" height="150" viewBox="0 0 320 150" aria-hidden="true" font-family="Open Sans, sans-serif" font-size="5" fill="#444">
    <g stroke="#e0e0e0" stroke-width=".6"><line x1="26" y1="5" x2="26" y2="125"/><line x1="70" y1="5" x2="70" y2="125"/><line x1="114" y1="5" x2="114" y2="125"/><line x1="158" y1="5" x2="158" y2="125"/><line x1="202" y1="5" x2="202" y2="125"/></g>
    <text x="4" y="25">2017</text><text x="4" y="52">2016</text><text x="4" y="79">2015</text><text x="4" y="106">2014</text>
    <rect x="26" y="18" width="60" height="4" fill="#7c2d22"/><rect x="26" y="24" width="148" height="4" fill="#262626"/>
    <rect x="26" y="45" width="40" height="4" fill="#7c2d22"/><rect x="26" y="51" width="100" height="4" fill="#262626"/>
    <rect x="26" y="72" width="160" height="4" fill="#7c2d22"/><rect x="26" y="78" width="54" height="4" fill="#262626"/>
    <rect x="26" y="99" width="66" height="4" fill="#7c2d22"/><rect x="26" y="105" width="124" height="4" fill="#262626"/>
    <text x="22" y="133">0</text><text x="64" y="133">50</text><text x="106" y="133">100</text><text x="150" y="133">150</text><text x="194" y="133">200</text><text x="236" y="133">250</text>
    <rect x="240" y="14" width="4" height="4" fill="#7c2d22"/><text x="248" y="18" font-weight="600">Title Text</text>
    <text x="248" y="26" font-size="4">Lorem ipsum dolor sit amet</text>
    <rect x="240" y="42" width="4" height="4" fill="#262626"/><text x="248" y="46" font-weight="600">Title Text</text>
    <text x="248" y="54" font-size="4">Lorem ipsum dolor sit amet</text>
    <rect x="240" y="70" width="4" height="4" fill="#8a8a8a"/><text x="248" y="74" font-weight="600">Title Text</text>
    <text x="248" y="82" font-size="4">Lorem ipsum dolor sit amet</text>
  </svg>
  <div class="foot"><span class="copy">© Copyright text here</span><span class="num">8</span></div>
</section>

<!-- 15 slide header with image -->
<section class="slide">
  <div class="photo" role="img" aria-label="Photograph of a construction crane" style="left:0;top:0;width:358px;height:258px;clip-path:polygon(230px 0,358px 0,358px 258px,180px 258px);background:linear-gradient(160deg,#e6e6e6,#a7a7a7 50%,#5c5c5c)"></div>
  <div class="hdr">SLIDE HEADER</div>
  <div class="brand">Kestrel<br>Properties</div>
  <p class="abs p" style="left:22px;top:56px;width:150px;font-size:6.3px">Lorem ipsum dolor sit amet, consectetur adipisicing elit, sed do eiusmod tempor incididunt ut labore et dolore magna aliqua. Ut enim ad minim veniam, quis nostrud exercitation ullamco laboris nisi ut aliquip ex ea commodo consequat. Duis aute irure dolor in reprehenderit in voluptate velit esse cillum dolore eu fugiat nulla pariatur. Excepteur sint occaecat cupidatat non proident, sunt in culpa qui officia deserunt mollit anim id est laborum.</p>
  <div class="foot"><span class="copy">© Copyright text here</span><span class="num">9</span></div>
</section>

<!-- 16 collage -->
<section class="slide">
  <div class="hdr">SLIDE HEADER</div>
  <div class="brand">Kestrel<br>Properties</div>
  <div class="photo" role="img" aria-label="Photograph of townhouses" style="left:26px;top:70px;width:70px;height:65px;background:linear-gradient(150deg,#c9a9a3,#8c5d55)"></div>
  <div class="abs" style="left:99px;top:70px;width:70px;height:65px;background:var(--charcoal);padding:8px"><p class="p w b" style="color:#fff;font-size:6px">Lorem ipsum dolor sit amet, consectetur adipisicing elit</p></div>
  <div class="photo" role="img" aria-label="Photograph of a commercial building" style="left:172px;top:70px;width:160px;height:65px;background:linear-gradient(150deg,#caa7a0,#8a5a52)"></div>
  <div class="abs" style="left:26px;top:138px;width:70px;height:65px;background:var(--charcoal);padding:8px"><p class="p w" style="font-weight:700;font-size:6px">Lorem ipsum dolor sit amet, consectetur adipisicing elit</p></div>
  <div class="photo" role="img" aria-label="Photograph of a crane on a site" style="left:99px;top:138px;width:70px;height:65px;background:linear-gradient(150deg,#d6b9b3,#9c6e66)"></div>
  <p class="abs p" style="left:176px;top:142px;width:156px;font-size:5.6px">Lorem ipsum dolor sit amet, consectetur adipisicing elit, sed do eiusmod tempor incididunt ut labore et dolore magna aliqua. Ut enim ad minim veniam, quis nostrud exercitation ullamco laboris nisi ut aliquip ex ea commodo consequat.</p>
  <div class="foot"><span class="copy">© Copyright text here</span><span class="num">10</span></div>
</section>

<!-- 17 column chart -->
<section class="slide">
  <div class="hdr">SLIDE HEADER</div>
  <div class="brand">Kestrel<br>Properties</div>
  <svg class="abs" style="left:16px;top:62px" width="160" height="150" viewBox="0 0 160 150" aria-hidden="true" font-family="Open Sans, sans-serif" font-size="4" fill="#444">
    <g stroke="#e4e4e4" stroke-width=".5"><line x1="8" y1="20" x2="150" y2="20"/><line x1="8" y1="50" x2="150" y2="50"/><line x1="8" y1="80" x2="150" y2="80"/><line x1="8" y1="110" x2="150" y2="110"/></g>
    <rect x="14" y="34" width="7" height="76" fill="#7c2d22"/><rect x="22" y="70" width="7" height="40" fill="#262626"/><rect x="30" y="74" width="7" height="36" fill="#8a8a8a"/>
    <rect x="48" y="54" width="7" height="56" fill="#7c2d22"/><rect x="56" y="78" width="7" height="32" fill="#262626"/><rect x="64" y="74" width="7" height="36" fill="#8a8a8a"/>
    <rect x="82" y="50" width="7" height="60" fill="#7c2d22"/><rect x="90" y="74" width="7" height="36" fill="#262626"/><rect x="98" y="52" width="7" height="58" fill="#8a8a8a"/>
    <rect x="116" y="30" width="7" height="80" fill="#7c2d22"/><rect x="124" y="62" width="7" height="48" fill="#262626"/><rect x="132" y="24" width="7" height="86" fill="#8a8a8a"/>
    <text x="14" y="117">Category 1</text><text x="48" y="117">Category 2</text><text x="82" y="117">Category 3</text><text x="116" y="117">Category 4</text>
    <rect x="30" y="134" width="4" height="4" fill="#7c2d22"/><text x="36" y="138">Title Text</text>
    <rect x="66" y="134" width="4" height="4" fill="#262626"/><text x="72" y="138">Title Text</text>
    <rect x="102" y="134" width="4" height="4" fill="#8a8a8a"/><text x="108" y="138">Title Text</text>
  </svg>
  <p class="abs p" style="left:184px;top:60px;width:152px;font-size:5.3px">Lorem ipsum dolor sit amet, consectetur adipisicing elit, sed do eiusmod tempor incididunt ut labore et dolore magna aliqua. Ut enim ad minim veniam, quis nostrud exercitation ullamco laboris nisi ut aliquip ex ea commodo consequat. Duis aute irure dolor in reprehenderit in voluptate velit esse cillum dolore eu fugiat nulla pariatur. Excepteur sint occaecat cupidatat non proident, sunt in culpa qui officia deserunt mollit anim id est laborum. Sed ut perspiciatis unde omnis iste natus error sit voluptatem accusantium doloremque laudantium, totam rem aperiam.</p>
  <div class="foot"><span class="copy">© Copyright text here</span><span class="num">11</span></div>
</section>

<!-- 18 cycle diagram -->
<section class="slide">
  <div class="hdr">SLIDE HEADER</div>
  <div class="brand">Kestrel<br>Properties</div>
  <svg class="abs" style="left:0;top:0" width="358" height="269" viewBox="0 0 358 269" aria-hidden="true">
    <g fill="none" stroke="#7c2d22" stroke-width=".7"><polyline points="118,78 150,78 158,96"/><polyline points="240,78 208,78 200,96"/><polyline points="118,168 150,168 158,150"/><polyline points="240,168 208,168 200,150"/></g>
    <circle cx="179" cy="123" r="32" fill="none" stroke="#7c2d22" stroke-width="16" stroke-dasharray="46 4.3"/>
    <circle cx="179" cy="123" r="22" fill="#fff"/>
  </svg>
  <div class="abs" style="left:22px;top:66px;width:100px"><div class="h6 m" style="font-size:6.5px">Text Title</div><p class="p" style="font-size:5.2px">Lorem ipsum dolor sit amet, consectetur adipisicing elit, sed do eiusmod tempor incididunt ut labore et dolore</p></div>
  <div class="abs" style="left:244px;top:66px;width:100px"><div class="h6" style="font-size:6.5px">Text Title</div><p class="p" style="font-size:5.2px">Lorem ipsum dolor sit amet, consectetur adipisicing elit, sed do eiusmod tempor incididunt ut labore et dolore</p></div>
  <div class="abs" style="left:22px;top:162px;width:100px"><div class="h6" style="font-size:6.5px">Text Title</div><p class="p" style="font-size:5.2px">Lorem ipsum dolor sit amet, consectetur adipisicing elit, sed do eiusmod tempor incididunt ut labore et dolore</p></div>
  <div class="abs" style="left:244px;top:162px;width:100px"><div class="h6 m" style="font-size:6.5px">Text Title</div><p class="p" style="font-size:5.2px">Lorem ipsum dolor sit amet, consectetur adipisicing elit, sed do eiusmod tempor incididunt ut labore et dolore</p></div>
  <div class="foot"><span class="copy">© Copyright text here</span><span class="num">12</span></div>
</section>

<!-- 19 team -->
<section class="slide">
  <div class="hdr">OUR TEAM</div>
  <div class="brand">Kestrel<br>Properties</div>
  <div class="abs" style="left:22px;top:48px;width:100px">
    <div class="photo" role="img" aria-label="Team member portrait photograph" style="position:relative;left:14px;width:54px;height:46px;border:2px solid var(--maroon);background:linear-gradient(160deg,#d8dde3,#9aa3ad)"></div>
    <div style="font:700 8.5px/1 'Open Sans',sans-serif;color:var(--maroon);margin-top:8px">Jonathan Doe</div>
    <p class="p" style="font-size:5.3px;margin-top:4px">Lorem ipsum dolor sit amet, consectetur adipisicing elit, sed do eiusmod tempor incididunt ut labore et dolore magna aliqua.</p>
    <p class="p" style="font-size:5.3px;margin-top:4px">Ut enim ad minim veniam, quis nostrud exercitation ullamco laboris nisi ut aliquip ex ea commodo consequat.</p>
  </div>
  <div class="abs" style="left:130px;top:48px;width:100px">
    <div class="photo" role="img" aria-label="Team member portrait photograph" style="position:relative;left:14px;width:54px;height:46px;border:2px solid var(--maroon);background:linear-gradient(160deg,#d8dde3,#9aa3ad)"></div>
    <div style="font:700 8.5px/1 'Open Sans',sans-serif;color:var(--maroon);margin-top:8px">Jonathan Doe</div>
    <p class="p" style="font-size:5.3px;margin-top:4px">Lorem ipsum dolor sit amet, consectetur adipisicing elit, sed do eiusmod tempor incididunt ut labore et dolore magna aliqua.</p>
    <p class="p" style="font-size:5.3px;margin-top:4px">Ut enim ad minim veniam, quis nostrud exercitation ullamco laboris nisi ut aliquip ex ea commodo consequat.</p>
  </div>
  <div class="abs" style="left:238px;top:48px;width:100px">
    <div class="photo" role="img" aria-label="Team member portrait photograph" style="position:relative;left:14px;width:54px;height:46px;border:2px solid var(--maroon);background:linear-gradient(160deg,#d8dde3,#9aa3ad)"></div>
    <div style="font:700 8.5px/1 'Open Sans',sans-serif;color:var(--maroon);margin-top:8px">Jonathan Doe</div>
    <p class="p" style="font-size:5.3px;margin-top:4px">Lorem ipsum dolor sit amet, consectetur adipisicing elit, sed do eiusmod tempor incididunt ut labore et dolore magna aliqua.</p>
    <p class="p" style="font-size:5.3px;margin-top:4px">Ut enim ad minim veniam, quis nostrud exercitation ullamco laboris nisi ut aliquip ex ea commodo consequat.</p>
  </div>
  <div class="foot"><span class="copy">© Copyright text here</span><span class="num">13</span></div>
</section>

<!-- 20 three columns on image -->
<section class="slide">
  <div class="photo" role="img" aria-label="Maroon-tinted photograph of a building" style="inset:0;background:linear-gradient(150deg,#8d3a2f,#6a2720)"></div>
  <div class="hdr light">HEADING TEXT GOES HERE</div>
  <div class="brand light">Kestrel<br>Properties</div>
  <div class="abs" style="left:22px;top:76px;width:96px"><div class="h6 w" style="font-size:7px">PLACE TITLE TEXT</div><p class="p w" style="font-size:4.8px;margin-top:5px">Lorem ipsum dolor sit amet, consectetur adipisicing elit, sed do eiusmod tempor incididunt ut labore et dolore magna aliqua. Ut enim ad minim veniam, quis nostrud exercitation ullamco laboris nisi ut aliquip ex ea commodo consequat. Duis aute irure dolor in reprehenderit in voluptate velit esse cillum dolore eu fugiat nulla pariatur. Excepteur sint occaecat cupidatat non proident, sunt in culpa qui officia deserunt mollit anim.</p></div>
  <div class="abs" style="left:131px;top:76px;width:96px"><div class="h6 w" style="font-size:7px">PLACE TITLE TEXT</div><p class="p w" style="font-size:4.8px;margin-top:5px">Lorem ipsum dolor sit amet, consectetur adipisicing elit, sed do eiusmod tempor incididunt ut labore et dolore magna aliqua. Ut enim ad minim veniam, quis nostrud exercitation ullamco laboris nisi ut aliquip ex ea commodo consequat. Duis aute irure dolor in reprehenderit in voluptate velit esse cillum dolore eu fugiat nulla pariatur. Excepteur sint occaecat cupidatat non proident, sunt in culpa qui officia deserunt mollit anim.</p></div>
  <div class="abs" style="left:240px;top:76px;width:96px"><div class="h6 w" style="font-size:7px">PLACE TITLE TEXT</div><p class="p w" style="font-size:4.8px;margin-top:5px">Lorem ipsum dolor sit amet, consectetur adipisicing elit, sed do eiusmod tempor incididunt ut labore et dolore magna aliqua. Ut enim ad minim veniam, quis nostrud exercitation ullamco laboris nisi ut aliquip ex ea commodo consequat. Duis aute irure dolor in reprehenderit in voluptate velit esse cillum dolore eu fugiat nulla pariatur. Excepteur sint occaecat cupidatat non proident, sunt in culpa qui officia deserunt mollit anim.</p></div>
  <div class="foot"><span class="copy">© Copyright text here</span><span class="num">14</span></div>
</section>

<!-- 21 text + bullets + image -->
<section class="slide">
  <div class="hdr">HEADING TEXT GOES HERE</div>
  <p class="abs p" style="left:22px;top:64px;width:190px;font-size:7px">Lorem ipsum dolor sit amet, consectetur adipisicing elit, sed do eiusmod tempor incididunt ut labore et dolore magna aliqua. Ut enim ad minim veniam, quis nostrud exercitation.</p>
  <ul class="abs" style="left:26px;top:122px;width:190px;list-style:none">
    <li class="p" style="font-size:7px;line-height:2.2"><span style="color:var(--maroon)">•</span> Lorem ipsum dolor sit amet.</li>
    <li class="p" style="font-size:7px;line-height:2.2"><span style="color:var(--maroon)">•</span> Consectetur adipisicing elit sed do.</li>
    <li class="p" style="font-size:7px;line-height:2.2"><span style="color:var(--maroon)">•</span> Eiusmod tempor incididunt ut.</li>
    <li class="p" style="font-size:7px;line-height:2.2"><span style="color:var(--maroon)">•</span> Labore et dolore magna aliqua.</li>
  </ul>
  <div class="photo" role="img" aria-label="Photograph of a modern apartment block" style="left:226px;top:92px;width:110px;height:100px;background:linear-gradient(180deg,#c8dcef,#8e8e8e 55%,#5e4a3f)"></div>
  <div class="foot"><span class="copy">© Copyright text here</span><span class="num">15</span></div>
</section>

<!-- 22 image + dark panel -->
<section class="slide">
  <div class="hdr">HEADING TEXT GOES HERE</div>
  <div class="brand">Kestrel<br>Properties</div>
  <div class="photo" role="img" aria-label="Photograph of a multi-storey building under blue sky" style="left:0;top:50px;width:186px;height:208px;background:linear-gradient(180deg,#cfe0f0,#9aa2ad 50%,#4f4a48)"></div>
  <div class="abs" style="left:186px;top:50px;width:172px;height:208px;background:var(--charcoal);padding:60px 16px 0 20px">
    <div class="h6" style="color:var(--maroon-soft);font-size:7px">PLACE TITLE TEXT</div>
    <p class="p w" style="font-size:5.2px;margin-top:3px">Lorem ipsum dolor sit amet, consectetur adipisicing elit, sed do eiusmod tempor incididunt ut labore et dolore magna aliqua. Ut enim ad minim veniam, quis nostrud exercitation ullamco laboris nisi ut aliquip ex ea commodo consequat.</p>
  </div>
  <div class="foot"><span class="copy">© Copyright text here</span><span class="num">16</span></div>
</section>

<!-- 23 text + geometric -->
<section class="slide">
  <div class="photo" role="img" aria-label="Faint greyscale photograph of a building" style="left:0;top:0;width:358px;height:258px;clip-path:polygon(200px 0,358px 0,358px 258px,230px 258px);background:linear-gradient(160deg,#efefef,#cfcfcf)"></div>
  <svg class="fill" viewBox="0 0 358 269" aria-hidden="true">
    <polygon points="210,0 358,0 270,130" fill="#7c2d22" opacity=".55"/>
    <polygon points="270,130 358,0 358,258" fill="#8a8a8a" opacity=".9"/>
    <polygon points="270,130 358,258 180,258" fill="#7c2d22"/>
  </svg>
  <div class="hdr">HEADING TEXT</div>
  <p class="abs p" style="left:22px;top:98px;width:160px;font-size:6.6px">Lorem ipsum dolor sit amet, consectetur adipisicing elit, sed do eiusmod tempor incididunt ut labore et dolore magna aliqua. Ut enim ad minim veniam, quis nostrud exercitation ullamco laboris nisi ut aliquip ex ea commodo consequat.</p>
  <div class="foot"><span class="copy">© Copyright text here</span><span class="num">17</span></div>
</section>

<!-- 24 thank you -->
<section class="slide">
  <svg class="fill" viewBox="0 0 358 269" aria-hidden="true">
    <polygon points="150,0 358,0 358,10 260,130" fill="#7c2d22"/>
    <polygon points="260,130 358,10 358,250" fill="#262626"/>
    <polygon points="260,130 358,250 358,269 130,269" fill="#7c2d22"/>
  </svg>
  <div class="abs brand-lg" style="left:20px;top:30px;font-size:15px">Kestrel<br>Properties</div>
  <div class="abs" style="left:20px;top:110px;font:700 19px/1 'Open Sans',sans-serif;color:var(--maroon)">THANK YOU</div>
  <div class="abs" style="left:20px;top:131px;font:400 14px/1 'Open Sans',sans-serif;color:var(--ink)">For Your Time</div>
  <div class="abs" style="left:20px;top:168px;font:700 10px/1 'Open Sans',sans-serif;color:var(--maroon)">Contact Us</div>
  <div class="abs" style="left:20px;top:184px;font:400 5px/2.4 'Open Sans',sans-serif;color:var(--text)">
    <div><svg width="7" height="7" viewBox="0 0 10 10" style="vertical-align:middle;margin-right:5px" aria-hidden="true"><circle cx="5" cy="5" r="5" fill="#7c2d22"/><path d="M3 2.5l1.2 1.2-.6.8a4 4 0 0 0 2 2l.8-.6L7.5 7 6.8 7.8C4.5 7.5 2.5 5.5 2.2 3.2z" fill="#fff"/></svg>+27 12 345 6789</div>
    <div><svg width="7" height="7" viewBox="0 0 10 10" style="vertical-align:middle;margin-right:5px" aria-hidden="true"><circle cx="5" cy="5" r="5" fill="#7c2d22"/><rect x="2.5" y="3.3" width="5" height="3.4" fill="none" stroke="#fff" stroke-width=".7"/><polyline points="2.5,3.3 5,5.3 7.5,3.3" fill="none" stroke="#fff" stroke-width=".7"/></svg>info@kestrelprop.co.za</div>
    <div><svg width="7" height="7" viewBox="0 0 10 10" style="vertical-align:middle;margin-right:5px" aria-hidden="true"><circle cx="5" cy="5" r="5" fill="#7c2d22"/><circle cx="5" cy="5" r="2.5" fill="none" stroke="#fff" stroke-width=".7"/><line x1="2.5" y1="5" x2="7.5" y2="5" stroke="#fff" stroke-width=".6"/></svg>www.kestrelprop.co.za</div>
    <div><svg width="7" height="7" viewBox="0 0 10 10" style="vertical-align:middle;margin-right:5px" aria-hidden="true"><circle cx="5" cy="5" r="5" fill="#7c2d22"/><path d="M5 8C3.6 6.2 3 5.3 3 4.3a2 2 0 0 1 4 0c0 1-.6 1.9-2 3.7z" fill="#fff"/></svg>Street No., Location</div>
  </div>
</section>

</main>
</body>
</html>
```